Birthday Calendar: Dec 1 - Nov 30

This calendar should have three parts. First the center should contain an annual calendar beginning December 1, 2019 and going through November 30, 2020. I'm picturing the months and date numbers - no need for individual boxes for each day. Second, above the calendar should be blank space (intended for people to write words of advise and love). Third, beneath the calendar space will be several statements about the year (i.e. "If you have client meetings four times a month, you'll meet with 36 clients." "If you kiss your kids only once each day, that's 1,460 kisses.") I don't have an exact overall size of the calendar in mind, but definitely know it will need to be bigger than 8.5"x11"

Target Market(s)

Wife - Her birthday is November 30, so this is a calendar to mark the time from one birthday to the next.

Font styles to use
Serif

Colors

Designer to choose colors to be used in the design.

Requirements
Must have
• The three different sections listed in the description. There will be 12 people handwriting simple phrases of advise (for how to have the best year) at the top, so there should be enough room for that. At the top it should say "These are the Days"
• I will provide the complete set of statements that will appear at the bottom of the calendar. There will be 10 (or less) statements total, sort of like the ones provided in the description. Let me know when you want those statements.

```html
<!DOCTYPE html>
<html lang="en">
<head>
<meta charset="utf-8">
<title>These are the Days – Birthday Calendar</title>
<link rel="stylesheet" href="https://fonts.googleapis.com/css2?family=Pinyon+Script&family=Merriweather:wght@700;900&family=Roboto+Condensed:wght@700&display=swap">
<style>
  :root{
    --crimson:#9b1a3d;
    --navy:#1d2550;
    --ink:#1f1f1f;
    --sage:#dde6bf;
    --mist:#d4eae8;
    --paper:#ffffff;
  }
  *{box-sizing:border-box;margin:0;padding:0}
  html,body{width:776px;height:1200px;overflow:hidden}
  body{
    position:relative;
    background:linear-gradient(to bottom,var(--paper) 0,var(--paper) 742px,#c9788d 820px,#ad3a58 880px,var(--crimson) 960px,var(--crimson) 100%);
    font-family:'Merriweather',Georgia,serif;
  }
  .title{
    position:absolute;inset:0 0 auto 0;height:280px;
    font-family:'Pinyon Script',cursive;color:var(--crimson);font-weight:400;
  }
  .title span{position:absolute;white-space:nowrap;line-height:1}
  .title .line-1{left:56px;top:34px;font-size:118px}
  .title .line-2{left:322px;top:148px;font-size:118px}

  .year{
    position:absolute;left:70px;top:517px;width:636px;
    display:grid;grid-template-columns:repeat(4,159px);row-gap:13px;
  }
  .month{
    height:118px;padding:3px 3px 0;
    border-radius:4px 4px 10px 10px;
    box-shadow:0 3px 2px rgba(0,0,0,.65);
  }
  .sage{background:var(--sage)}
  .mist{background:var(--mist)}
  .month h2{
    font-size:11.5px;font-weight:900;color:var(--crimson);
    text-align:center;line-height:14px;letter-spacing:.1px;
  }
  .days{
    display:grid;grid-template-columns:repeat(7,1fr);
    text-align:center;font-size:11px;font-weight:900;color:var(--ink);line-height:14.2px;
  }
  .days .dow{
    font-family:'Roboto Condensed',Arial,sans-serif;font-size:10.5px;color:var(--navy);
    text-decoration:underline;text-underline-offset:1px;line-height:13px;
  }
  .s1{grid-column-start:2}.s2{grid-column-start:3}.s3{grid-column-start:4}
  .s4{grid-column-start:5}.s5{grid-column-start:6}.s6{grid-column-start:7}

  .facts{position:absolute;left:54px;top:932px;list-style:none;color:var(--paper)}
  .facts li{font-size:11px;font-weight:700;line-height:27.5px;white-space:nowrap}
  .facts li:nth-child(2){padding-left:17.5px}
  .facts li:nth-child(3){padding-left:35px}
  .facts li:nth-child(4){padding-left:52.5px}
  .facts li:nth-child(5){padding-left:70px}
  .facts li:nth-child(6){padding-left:87.5px}
  .facts li:nth-child(7){padding-left:105px}
  .facts li:nth-child(8){padding-left:122.5px}
</style>
</head>
<body>
<h1 class="title"><span class="line-1">These are</span><span class="line-2">the Days</span></h1>

<section class="year" aria-label="Calendar December 2019 to November 2020">
  <div class="month sage"><h2>DECEMBER 2019</h2><div class="days">
    <span class="dow">Su</span><span class="dow">Mo</span><span class="dow">Tu</span><span class="dow">We</span><span class="dow">Th</span><span class="dow">Fr</span><span class="dow">Sa</span>
    <span>1</span><span>2</span><span>3</span><span>4</span><span>5</span><span>6</span><span>7</span><span>8</span><span>9</span><span>10</span><span>11</span><span>12</span><span>13</span><span>14</span><span>15</span><span>16</span><span>17</span><span>18</span><span>19</span><span>20</span><span>21</span><span>22</span><span>23</span><span>24</span><span>25</span><span>26</span><span>27</span><span>28</span><span>29</span><span>30</span><span>31</span>
  </div></div>
  <div class="month mist"><h2>JANUARY 2020</h2><div class="days">
    <span class="dow">Su</span><span class="dow">Mo</span><span class="dow">Tu</span><span class="dow">We</span><span class="dow">Th</span><span class="dow">Fr</span><span class="dow">Sa</span>
    <span class="s3">1</span><span>2</span><span>3</span><span>4</span><span>5</span><span>6</span><span>7</span><span>8</span><span>9</span><span>10</span><span>11</span><span>12</span><span>13</span><span>14</span><span>15</span><span>16</span><span>17</span><span>18</span><span>19</span><span>20</span><span>21</span><span>22</span><span>23</span><span>24</span><span>25</span><span>26</span><span>27</span><span>28</span><span>29</span><span>30</span><span>31</span>
  </div></div>
  <div class="month sage"><h2>FEBRUARY 2020</h2><div class="days">
    <span class="dow">Su</span><span class="dow">Mo</span><span class="dow">Tu</span><span class="dow">We</span><span class="dow">Th</span><span class="dow">Fr</span><span class="dow">Sa</span>
    <span class="s6">1</span><span>2</span><span>3</span><span>4</span><span>5</span><span>6</span><span>7</span><span>8</span><span>9</span><span>10</span><span>11</span><span>12</span><span>13</span><span>14</span><span>15</span><span>16</span><span>17</span><span>18</span><span>19</span><span>20</span><span>21</span><span>22</span><span>23</span><span>24</span><span>25</span><span>26</span><span>27</span><span>28</span><span>29</span>
  </div></div>
  <div class="month mist"><h2>MARCH 2020</h2><div class="days">
    <span class="dow">Su</span><span class="dow">Mo</span><span class="dow">Tu</span><span class="dow">We</span><span class="dow">Th</span><span class="dow">Fr</span><span class="dow">Sa</span>
    <span>1</span><span>2</span><span>3</span><span>4</span><span>5</span><span>6</span><span>7</span><span>8</span><span>9</span><span>10</span><span>11</span><span>12</span><span>13</span><span>14</span><span>15</span><span>16</span><span>17</span><span>18</span><span>19</span><span>20</span><span>21</span><span>22</span><span>23</span><span>24</span><span>25</span><span>26</span><span>27</span><span>28</span><span>29</span><span>30</span><span>31</span>
  </div></div>

  <div class="month mist"><h2>APRIL 2020</h2><div class="days">
    <span class="dow">Su</span><span class="dow">Mo</span><span class="dow">Tu</span><span class="dow">We</span><span class="dow">Th</span><span class="dow">Fr</span><span class="dow">Sa</span>
    <span class="s3">1</span><span>2</span><span>3</span><span>4</span><span>5</span><span>6</span><span>7</span><span>8</span><span>9</span><span>10</span><span>11</span><span>12</span><span>13</span><span>14</span><span>15</span><span>16</span><span>17</span><span>18</span><span>19</span><span>20</span><span>21</span><span>22</span><span>23</span><span>24</span><span>25</span><span>26</span><span>27</span><span>28</span><span>29</span><span>30</span>
  </div></div>
  <div class="month sage"><h2>MAY 2020</h2><div class="days">
    <span class="dow">Su</span><span class="dow">Mo</span><span class="dow">Tu</span><span class="dow">We</span><span class="dow">Th</span><span class="dow">Fr</span><span class="dow">Sa</span>
    <span class="s5">1</span><span>2</span><span>3</span><span>4</span><span>5</span><span>6</span><span>7</span><span>8</span><span>9</span><span>10</span><span>11</span><span>12</span><span>13</span><span>14</span><span>15</span><span>16</span><span>17</span><span>18</span><span>19</span><span>20</span><span>21</span><span>22</span><span>23</span><span>24</span><span>25</span><span>26</span><span>27</span><span>28</span><span>29</span><span>30</span><span>31</span>
  </div></div>
  <div class="month mist"><h2>JUNE 2020</h2><div class="days">
    <span class="dow">Su</span><span class="dow">Mo</span><span class="dow">Tu</span><span class="dow">We</span><span class="dow">Th</span><span class="dow">Fr</span><span class="dow">Sa</span>
    <span class="s1">1</span><span>2</span><span>3</span><span>4</span><span>5</span><span>6</span><span>7</span><span>8</span><span>9</span><span>10</span><span>11</span><span>12</span><span>13</span><span>14</span><span>15</span><span>16</span><span>17</span><span>18</span><span>19</span><span>20</span><span>21</span><span>22</span><span>23</span><span>24</span><span>25</span><span>26</span><span>27</span><span>28</span><span>29</span><span>30</span>
  </div></div>
  <div class="month sage"><h2>JULY 2020</h2><div class="days">
    <span class="dow">Su</span><span class="dow">Mo</span><span class="dow">Tu</span><span class="dow">We</span><span class="dow">Th</span><span class="dow">Fr</span><span class="dow">Sa</span>
    <span class="s3">1</span><span>2</span><span>3</span><span>4</span><span>5</span><span>6</span><span>7</span><span>8</span><span>9</span><span>10</span><span>11</span><span>12</span><span>13</span><span>14</span><span>15</span><span>16</span><span>17</span><span>18</span><span>19</span><span>20</span><span>21</span><span>22</span><span>23</span><span>24</span><span>25</span><span>26</span><span>27</span><span>28</span><span>29</span><span>30</span><span>31</span>
  </div></div>

  <div class="month sage"><h2>AUGUST 2020</h2><div class="days">
    <span class="dow">Su</span><span class="dow">Mo</span><span class="dow">Tu</span><span class="dow">We</span><span class="dow">Th</span><span class="dow">Fr</span><span class="dow">Sa</span>
    <span class="s6">1</span><span>2</span><span>3</span><span>4</span><span>5</span><span>6</span><span>7</span><span>8</span><span>9</span><span>10</span><span>11</span><span>12</span><span>13</span><span>14</span><span>15</span><span>16</span><span>17</span><span>18</span><span>19</span><span>20</span><span>21</span><span>22</span><span>23</span><span>24</span><span>25</span><span>26</span><span>27</span><span>28</span><span>29</span><span>30</span><span>31</span>
  </div></div>
  <div class="month mist"><h2>SEPTEMBER 2020</h2><div class="days">
    <span class="dow">Su</span><span class="dow">Mo</span><span class="dow">Tu</span><span class="dow">We</span><span class="dow">Th</span><span class="dow">Fr</span><span class="dow">Sa</span>
    <span class="s2">1</span><span>2</span><span>3</span><span>4</span><span>5</span><span>6</span><span>7</span><span>8</span><span>9</span><span>10</span><span>11</span><span>12</span><span>13</span><span>14</span><span>15</span><span>16</span><span>17</span><span>18</span><span>19</span><span>20</span><span>21</span><span>22</span><span>23</span><span>24</span><span>25</span><span>26</span><span>27</span><span>28</span><span>29</span><span>30</span>
  </div></div>
  <div class="month sage"><h2>OCTOBER 2020</h2><div class="days">
    <span class="dow">Su</span><span class="dow">Mo</span><span class="dow">Tu</span><span class="dow">We</span><span class="dow">Th</span><span class="dow">Fr</span><span class="dow">Sa</span>
    <span class="s4">1</span><span>2</span><span>3</span><span>4</span><span>5</span><span>6</span><span>7</span><span>8</span><span>9</span><span>10</span><span>11</span><span>12</span><span>13</span><span>14</span><span>15</span><span>16</span><span>17</span><span>18</span><span>19</span><span>20</span><span>21</span><span>22</span><span>23</span><span>24</span><span>25</span><span>26</span><span>27</span><span>28</span><span>29</span><span>30</span><span>31</span>
  </div></div>
  <div class="month mist"><h2>NOVEMBER 2020</h2><div class="days">
    <span class="dow">Su</span><span class="dow">Mo</span><span class="dow">Tu</span><span class="dow">We</span><span class="dow">Th</span><span class="dow">Fr</span><span class="dow">Sa</span>
    <span>1</span><span>2</span><span>3</span><span>4</span><span>5</span><span>6</span><span>7</span><span>8</span><span>9</span><span>10</span><span>11</span><span>12</span><span>13</span><span>14</span><span>15</span><span>16</span><span>17</span><span>18</span><span>19</span><span>20</span><span>21</span><span>22</span><span>23</span><span>24</span><span>25</span><span>26</span><span>27</span><span>28</span><span>29</span><span>30</span>
  </div></div>
</section>

<ul class="facts">
  <li>1,460 – the number of kisses given if you kiss each kid just once a day.</li>
  <li>12 – the number of events you’ll run if you coordinate one each month.</li>
  <li>52 – the people you’ve made time for if you meet with just one friend each week.</li>
  <li>20 – about the number of dates you could go on with Morgan if you got out every few weeks.</li>
  <li>260 – the number of family meals shared together if you have just 5 dinners a week.</li>
  <li>24 – the number of cups of coffee shared with your parents if they come over twice a month.</li>
  <li>156 – the number of workouts you can squeeze in if you just do it three times a week.</li>
  <li>4 – the number of days devoted entirely to you, if you take two hours a week just for yourself.</li>
</ul>
</body>
</html>
```